Bref créative
Business Cards, Stationery and Email signature for Luxury Brand
Kestral
I need double sided standard sized Business Card [3.5" x 2"]
Can use whatever font will look high end
Professional
Dennis L. Farrow
CEO/President
417 Larkspur Ave.
Suite 350
Cedar Vale, OR 90187
df@kestralinquiries.example
kestralinquiries.example
Please put in holder for this - Don't have number yet
Want to have plastic business card. All black on front of card with just logo. Back of Card will have all information. Black border on back might be nice showing starburst from logo on top and having line under logo on bottom border of card. Open to other ideas for back as well.
ALL INFORMATION WILL GO ON BACK OF CARD - Card will be plastic
Logo only on front

```html
<!DOCTYPE html>
<html lang="en">
<head>
<meta charset="utf-8">
<title>Kestral – Business Card</title>
<link href="https://fonts.googleapis.com/css2?family=Cinzel:wght@600&family=Arimo:wght@400;700&display=swap" rel="stylesheet">
<style>
  :root {
    --page: #1c1c1e;
    --card-top: #2a2a2c;
    --card-bottom: #050505;
    --silver: #d9d9dc;
    --silver-dim: #8d8d92;
    --text: #e6e6e8;
    --text-muted: #b4b4b8;
  }
  * { margin: 0; padding: 0; box-sizing: border-box; }
  html, body { width: 1200px; height: 869px; overflow: hidden; background: var(--page); }
  .canvas { position: relative; width: 1200px; height: 869px; }
  .card {
    position: absolute;
    width: 500px; height: 286px;
    background: linear-gradient(180deg, var(--card-top) 0%, var(--card-bottom) 70%);
    box-shadow: 0 10px 30px rgba(0,0,0,.6);
    overflow: hidden;
  }
  .card-front { left: 80px; top: 240px; }
  .card-back { left: 620px; top: 240px; }
  .card svg.swoosh { position: absolute; left: 0; top: 0; width: 500px; height: 286px; }
  .wordmark {
    position: absolute; left: 0; right: 0; text-align: center;
    font-family: "Cinzel", serif; font-weight: 600;
    color: var(--silver); letter-spacing: 3px;
  }
  .card-front .wordmark { top: 112px; font-size: 38px; }
  .card-back .wordmark { top: 26px; font-size: 22px; letter-spacing: 2px; }
  .holder {
    position: absolute; left: 34px; top: 152px;
    font-family: "Arimo", sans-serif; color: var(--text);
  }
  .holder-name { font-size: 15px; font-weight: 700; }
  .holder-title { font-size: 11px; color: var(--text-muted); margin-top: 3px; }
  .contact {
    position: absolute; left: 280px; top: 132px;
    font-family: "Arimo", sans-serif; font-size: 10.5px; line-height: 14px;
    font-style: normal; color: var(--text-muted);
  }
  .website-band {
    position: absolute; left: 0; right: 0; bottom: 0; height: 36px;
    background: linear-gradient(180deg, #151515, #000);
    border-top: 1px solid #3a3a3c;
    font-family: "Arimo", sans-serif; font-size: 10.5px; font-weight: 700;
    color: var(--text); text-align: center; line-height: 36px;
  }
  .signoff {
    position: absolute; left: 0; right: 0; top: 640px; text-align: center;
    font-family: "Cinzel", serif; font-weight: 600; font-size: 26px;
    letter-spacing: 3px; color: var(--silver);
  }
</style>
</head>
<body>
<main class="canvas">

  <section class="card card-front" aria-label="Card front">
    <svg class="swoosh" viewBox="0 0 500 286" aria-hidden="true">
      <defs>
        <linearGradient id="silverLine" x1="0" x2="1">
          <stop offset="0" stop-color="#d9d9dc" stop-opacity="0"/>
          <stop offset="0.6" stop-color="#d9d9dc"/>
          <stop offset="1" stop-color="#ffffff"/>
        </linearGradient>
      </defs>
      <path d="M40 60 Q260 20 500 30" fill="none" stroke="url(#silverLine)" stroke-width="3"/>
      <path d="M0 230 Q200 190 500 215 L500 230 Q220 205 0 250 Z" fill="#c9c9cc"/>
      <path d="M0 250 Q220 205 500 230 L500 286 L0 286 Z" fill="#0a0a0a"/>
    </svg>
    <div class="wordmark">KESTRAL</div>
  </section>

  <section class="card card-back" aria-label="Card back">
    <svg class="swoosh" viewBox="0 0 500 286" aria-hidden="true">
      <path d="M20 78 Q250 50 500 56 L500 62 Q250 60 20 82 Z" fill="#c9c9cc"/>
    </svg>
    <div class="wordmark">KESTRAL</div>
    <div class="holder">
      <p class="holder-name">Dennis L. Farrow</p>
      <p class="holder-title">CEO/President</p>
    </div>
    <address class="contact">
      417 Larkspur Ave.<br>
      Suite 350<br>
      Cedar Vale, OR 90187<br><br>
      800-000-0000<br>
      310-000-0000<br>
      df@kestralinquiries.example
    </address>
    <div class="website-band">kestralinquiries.example</div>
  </section>

  <div class="signoff">KESTRAL</div>

</main>
</body>
</html>
```